Bright Hall Meetings: Educators and Families joining forces for pupil growth.

This is a book that helps to prepare for and hold a standard conference that an educator would have with the parents of the students in the school. It is also about how to have problem-solving conferences around difficult issues using techniques from family therapy. Parent involvement is a key ingredient for student success, but most educators have no training in holding meetings with parents. This book fills that gap.
Updates

Need extra days to review

Target Market(s)

Teachers, principals, counselors, school psychologists, school nurses. Anyone who has conferences with the parents of their students.

Font styles to use
Sans Serif

Colors
85acd3
ffcf3e

Requirements
Must have
• I have several books coming up. I'd like something that could be carried over to the new ones without too many changes. They won't all be about education. I am a psychologist so most of my writings will cover subjects related to emotional intelligence.
Nice to have
• Something dignified that will pop out for those in the schools. I like the combination of a royal blue background with white and gold (not yellow) lettering.
Should not have
• I'd like it to be easy to read. Not too messy or too much stuff on the page.

```html
<!DOCTYPE html>
<html lang="en">
<head>
<meta charset="utf-8">
<title>Bright Hall Meetings – Book Cover</title>
<link href="https://fonts.googleapis.com/css2?family=Oswald:wght@400;500;600;700&display=swap" rel="stylesheet">
<style>
  :root {
    --navy-deep: #0a1a4a;
    --royal: #1c3a8f;
    --royal-light: #2a50ad;
    --gold-light: #f7e08a;
    --gold: #e3b54a;
    --gold-dark: #a8782a;
    --silver-light: #ffffff;
    --silver: #d9dde6;
    --silver-dark: #9aa3b5;
    --ink: #0d1c45;
    --white: #ffffff;
  }
  * { margin: 0; padding: 0; box-sizing: border-box; }
  html, body {
    width: 887px;
    height: 1200px;
    overflow: hidden;
    background: var(--navy-deep);
  }
  .book-cover {
    position: relative;
    width: 887px;
    height: 1200px;
    background: radial-gradient(ellipse 75% 60% at 55% 42%, var(--royal-light) 0%, var(--royal) 45%, var(--navy-deep) 100%);
    font-family: "Oswald", "Arial Narrow", sans-serif;
    text-align: center;
    overflow: hidden;
  }
  .title {
    position: absolute;
    top: 120px;
    left: 0;
    right: 0;
    text-transform: uppercase;
    font-weight: 700;
    line-height: 0.98;
  }
  .title span { display: block; }
  .title-gold {
    background: linear-gradient(180deg, var(--gold-light) 0%, var(--gold) 50%, var(--gold-dark) 100%);
    -webkit-background-clip: text;
    background-clip: text;
    color: transparent;
  }
  .title-silver {
    background: linear-gradient(180deg, var(--silver-light) 0%, var(--silver) 55%, var(--silver-dark) 100%);
    -webkit-background-clip: text;
    background-clip: text;
    color: transparent;
  }
  .title-line-1 { font-size: 205px; letter-spacing: 4px; }
  .title-line-2 { font-size: 215px; letter-spacing: 6px; }
  .title-line-3 { font-size: 150px; letter-spacing: 3px; margin-top: 6px; }

  .subtitle {
    position: absolute;
    top: 790px;
    left: 60px;
    right: 60px;
    text-transform: uppercase;
  }
  .subtitle-lead {
    color: var(--white);
    font-weight: 500;
    font-size: 40px;
    line-height: 1.25;
    letter-spacing: 1.5px;
  }
  .subtitle-accent {
    margin-top: 6px;
    font-size: 66px;
    font-weight: 700;
    letter-spacing: 2px;
    line-height: 1.1;
  }
  .author-band {
    position: absolute;
    left: 0;
    right: 0;
    bottom: 0;
    height: 175px;
    background: linear-gradient(180deg, var(--gold-light) 0%, var(--gold) 45%, var(--gold-dark) 100%);
    display: flex;
    align-items: center;
    justify-content: center;
  }
  .author-name {
    color: var(--ink);
    font-size: 78px;
    font-weight: 700;
    letter-spacing: 3px;
    text-transform: uppercase;
  }
</style>
</head>
<body>
  <main class="book-cover">
    <h1 class="title">
      <span class="title-line-1 title-gold">Bright</span>
      <span class="title-line-2 title-silver">Hall</span>
      <span class="title-line-3 title-gold">Meetings</span>
    </h1>
    <div class="subtitle">
      <p class="subtitle-lead">Educators and Families<br>joining forces for</p>
      <p class="subtitle-accent title-gold">Pupil Growth</p>
    </div>
    <footer class="author-band">
      <p class="author-name">Author Name</p>
    </footer>
  </main>
</body>
</html>
```